Help us stand out from the crowd - Pellingham Row

We are a luxury watch business and are looking to develop our own paperwork that we can issue with our watches etc. I am looking for the following documents to be designed: Invoice, Warranty card, Insurance valuation, instruction booklet and a small folder to keep it all in. Need it to be small though. I have attached some images of my friends ones that look fantastic.

Target Market(s)

High net worth watch enthusiasts

Requirements
Must have
• Must be clean, precise and very easy on the eye. Think Vorla but underpinned with a classic british feel.
Should not have
• Shouldn't be dark.

```html
<!DOCTYPE html>
<html lang="en">
<head>
<meta charset="utf-8">
<title>Insurance Valuation – Pellingham Row</title>
<link href="https://fonts.googleapis.com/css2?family=Urbanist:wght@300;400;500&family=Cinzel:wght@400&family=Cormorant+Garamond:wght@500&display=swap" rel="stylesheet">
<style>
  :root {
    --backdrop: #5e5e5e;
    --paper: #ffffff;
    --ink: #1d1d1d;
    --rule: #2e2e2e;
  }
  * { margin: 0; padding: 0; box-sizing: border-box; }
  html, body { width: 1200px; height: 1200px; overflow: hidden; background: var(--backdrop); }
  .sheet {
    position: absolute; left: 204px; top: 38px; width: 790px; height: 1113px;
    background: var(--paper); overflow: hidden; color: var(--ink);
    font-family: "Urbanist", sans-serif;
  }
  .sheet > * { position: absolute; line-height: 1; white-space: nowrap; }
  .title { left: 55px; top: 62px; font-size: 47px; font-weight: 300; letter-spacing: 0.2px; }
  .brand { left: 56px; top: 140px; font-family: "Cinzel", serif; font-size: 31px; letter-spacing: 4.4px; }
  .brand-rule { left: 56px; top: 182px; width: 370px; height: 1.5px; background: var(--rule); }
  .motto { left: 57px; top: 197px; font-family: "Cormorant Garamond", serif; font-weight: 500; font-size: 14.5px; letter-spacing: 2.8px; text-transform: uppercase; }
  .contact { left: 58px; top: 233px; font-size: 19.5px; font-weight: 300; line-height: 22px; letter-spacing: 0.1px; }
  .intro, .declaration { left: 58px; font-size: 19.5px; font-weight: 300; line-height: 23px; letter-spacing: 0.1px; }
  .intro { top: 330px; }
  .schedule-title { left: 0; width: 796px; top: 414px; text-align: center; font-size: 21px; font-weight: 500; letter-spacing: 0.3px; }
  .rule { left: 57px; width: 680px; height: 1.2px; background: var(--rule); }
  .col-head { top: 469px; font-size: 21px; font-weight: 500; letter-spacing: 0.2px; }
  .col-item { left: 59px; }
  .col-desc { left: 301px; }
  .col-price { left: 564px; }
  .col-total { right: 53px; }
  .total-rule { left: 472px; width: 265px; height: 1.2px; background: var(--rule); }
  .total-label { left: 488px; top: 821px; font-size: 21px; font-weight: 500; }
  .declaration { top: 905px; }
  .field-label { font-size: 21px; font-weight: 500; }
  .signed { right: 333px; top: 965px; }
  .dated { left: 59px; top: 1032px; }
  .day-of { left: 392px; top: 1032px; }
  .field-line { height: 1.2px; background: var(--rule); }
</style>
</head>
<body>
  <main class="sheet">
    <h1 class="title">INSURANCE VALUATION</h1>
    <div class="brand">Pellingham Row</div>
    <div class="brand-rule"></div>
    <p class="motto">“Precision kept, every hour well worn”</p>
    <p class="contact">www.pellinghamrow.co.uk &nbsp;| &nbsp; (+44) 01632 960418<br>Ashcombe Yard, Weald House, 9 Mill Lane, Lindfield RH99 4QT</p>

    <p class="intro">This valuation for insurance is based on values current at the under mentioned<br>date. It is valid only for the purpose specified above.</p>

    <h2 class="schedule-title">SCHEDULE</h2>
    <div class="rule" style="top:444px"></div>
    <span class="col-head col-item">Item Number</span>
    <span class="col-head col-desc">Description</span>
    <span class="col-head col-price">£</span>
    <span class="col-head col-total">TOTAL</span>
    <div class="rule" style="top:508px"></div>
    <div class="rule" style="top:547px"></div>
    <div class="rule" style="top:586px"></div>
    <div class="rule" style="top:624px"></div>
    <div class="rule" style="top:661px"></div>
    <div class="rule" style="top:699px"></div>
    <div class="rule" style="top:736px"></div>
    <div class="rule" style="top:774px"></div>

    <div class="total-rule" style="top:810px"></div>
    <span class="total-label">TOTAL</span>
    <div class="total-rule" style="top:847px"></div>

    <p class="declaration">I have examined the articles scheduled above and in my opinion the figures<br>given represent the value of such articles for the purpose stated.</p>

    <span class="field-label signed">Signed</span>
    <div class="field-line" style="left:472px;width:265px;top:982px"></div>

    <span class="field-label dated">Dated this</span>
    <div class="field-line" style="left:174px;width:195px;top:1047px"></div>
    <span class="field-label day-of">day of</span>
    <div class="field-line" style="left:472px;width:265px;top:1047px"></div>
  </main>
</body>
</html>
```